Business Card - connecting 2 souls and beggining the journey of self discovery

Logo on the front
with tag line

On the back list of services and contact details

Seminars
workshops
Coaching
podcasts

Daniel Porthwick
Health & Wellbeing Life Coach
0491 372 815
daniel@wovenpathwellness.example
wovenpathwellness.example

Industry/Entity Type

Life Coaching

Contact Information for Business Card

I like the use of colour from the logo to be used. I'm not a fan of white.

Requirements
Must have
• My tagline: The journey home starts with you
Nice to have
• Use of colour that is in the Woven Path Wellness logo

```html
<!DOCTYPE html>
<html lang="en">
<head>
<meta charset="utf-8">
<title>Woven Path Wellness – Business Card</title>
<link rel="stylesheet" href="https://fonts.googleapis.com/css2?family=Lato:wght@400;700&family=Arimo:ital,wght@0,400;0,700;1,400;1,700&display=swap">
<style>
  :root {
    --backdrop: #eceae6;
    --plum: #8a3366;
    --rose: #cf4a5f;
    --teal: #3aa79c;
    --green: #86c44a;
    --lime: #9fcd3c;
    --yellow: #f4e81c;
    --mark: #f29a3a;
    --shadow: rgba(40, 30, 40, 0.28);
  }
  * { box-sizing: border-box; margin: 0; padding: 0; }
  html, body { width: 1200px; height: 1200px; overflow: hidden; }
  body {
    background: var(--backdrop);
    position: relative;
    font-family: "Arimo", Arial, sans-serif;
    color: var(--yellow);
  }
  .card {
    position: absolute;
    left: 150px;
    width: 900px;
    height: 515px;
    box-shadow: 0 10px 28px var(--shadow);
    overflow: hidden;
  }
  .card--front {
    top: 55px;
    background: linear-gradient(90deg, var(--plum) 0%, var(--rose) 38%, var(--teal) 62%, var(--green) 100%);
  }
  .card--back {
    top: 630px;
    background: linear-gradient(90deg, var(--lime) 0%, var(--teal) 30%, var(--rose) 65%, var(--plum) 100%);
  }

  /* Front */
  .brand {
    position: absolute;
    top: 120px;
    left: 0;
    width: 100%;
    display: flex;
    align-items: center;
    justify-content: center;
    gap: 26px;
  }
  .brand__dot {
    width: 120px;
    height: 120px;
    border-radius: 50%;
    background: var(--mark);
    flex: none;
  }
  .brand__name {
    font-family: "Lato", sans-serif;
    font-weight: 700;
    font-size: 48px;
    color: var(--yellow);
    line-height: 1.1;
  }
  .tagline-front {
    position: absolute;
    top: 340px;
    width: 100%;
    text-align: center;
    font-family: "Lato", sans-serif;
    font-size: 50px;
    font-weight: 400;
    color: var(--yellow);
  }

  /* Back */
  .back-mark {
    position: absolute;
    top: 58px;
    right: 48px;
    display: flex;
    align-items: center;
    gap: 10px;
  }
  .back-mark__dot {
    width: 42px;
    height: 42px;
    border-radius: 50%;
    background: var(--mark);
  }
  .back-mark__name {
    font-family: "Arimo", sans-serif;
    font-weight: 700;
    font-size: 17px;
    color: var(--yellow);
  }
  .identity {
    position: absolute;
    top: 135px;
    right: 48px;
    text-align: left;
  }
  .identity__name {
    font-weight: 700;
    font-size: 30px;
    margin-bottom: 8px;
  }
  .identity__role {
    font-style: italic;
    font-size: 24px;
  }
  .details {
    position: absolute;
    top: 150px;
    left: 45px;
    font-style: italic;
    font-size: 21px;
    line-height: 1.3;
    list-style: none;
  }
  .tagline-back {
    position: absolute;
    left: 45px;
    bottom: 65px;
    font-weight: 700;
    font-style: italic;
    font-size: 33px;
  }
</style>
</head>
<body>

  <section class="card card--front" aria-label="Business card front">
    <div class="brand">
      <span class="brand__dot"></span>
      <span class="brand__name">Woven Path<br>Wellness</span>
    </div>
    <p class="tagline-front">Home of Holistic Health</p>
  </section>

  <section class="card card--back" aria-label="Business card back">
    <div class="back-mark">
      <span class="back-mark__dot"></span>
      <span class="back-mark__name">Woven Path Wellness</span>
    </div>

    <div class="identity">
      <p class="identity__name">Daniel Porthwick</p>
      <p class="identity__role">Health &amp; Wellbeing Life Coach</p>
    </div>

    <ul class="details">
      <li>Seminars, workshops</li>
      <li>Coaching, podcasts</li>
      <li>0491 372 815</li>
      <li>daniel@wovenpathwellness.example</li>
      <li>wovenpathwellness.example</li>
    </ul>

    <p class="tagline-back">The journey home starts with you......</p>
  </section>

</body>
</html>
```